Card design for Heating and Cooling company

this is for a heating and cooling company we recently updated our logo and need to update our cards. We attached our logo so you can incorporate it into the card. We specialize in residential and commercial furnace and air condition repairs. Have been in business since 2014.

Phone number 555.284.9137

We need the following phrases
:Repairs, Installations, and maintenance
:Quality work at reasonable prices
:residential/commercial
:Licensed &Insured
:Email Pinegrovehvac47@mailbox-example.com
Name: Teodor K (Ted)
Also on back side I would like my logo with wording :Thank you for your business and refferal

Industry/Entity Type

Hvac

Contact Information for Business Card

:residential/commercial
:Licensed & Insured
Name: Teodor K (Ted)
Number:555.284.9136

Requirements
Must have
• Blue and red colors
Nice to have
• Maybe a pic of a furnace or air conditioner

```html
<!DOCTYPE html>
<html lang="en">
<head>
<meta charset="utf-8">
<title>Pinegrove Heating &amp; Cooling – Business Cards</title>
<link rel="stylesheet" href="https://fonts.googleapis.com/css2?family=Lato:wght@400;700&display=swap">
<style>
  :root {
    --backdrop: #3a3431;
    --card: #111112;
    --card-edge: #1c1c1e;
    --ink: #f2f2f2;
    --blue: #1f9ee6;
    --red: #e5261c;
    --silver: #d9d9d9;
    --divider: #3a3a3c;
  }
  * { box-sizing: border-box; margin: 0; padding: 0; }
  html, body {
    width: 1200px; height: 844px; overflow: hidden;
    background: var(--backdrop);
    font-family: "Lato", Arial, sans-serif;
  }
  .stage {
    width: 1200px; height: 844px;
    display: flex; align-items: center; justify-content: center; gap: 40px;
  }
  .card {
    position: relative;
    width: 540px; height: 310px;
    background: var(--card);
    border: 1px solid var(--card-edge);
    box-shadow: 0 12px 30px rgba(0,0,0,.45);
    color: var(--ink);
    overflow: hidden;
  }
  /* Front */
  .card-front .brand {
    position: absolute; left: 24px; top: 90px; width: 220px;
    display: flex; align-items: center; justify-content: center; gap: 9px;
  }
  .brand-dot {
    width: 14px; height: 14px; border-radius: 50%; background: var(--blue); flex: none;
  }
  .brand-name {
    font-weight: 700; font-size: 30px; letter-spacing: .4px; color: var(--ink);
  }
  .card-front .divider {
    position: absolute; left: 258px; top: 40px; width: 1px; height: 130px;
    background: var(--divider);
  }
  .contact { position: absolute; left: 278px; right: 20px; top: 52px; }
  .contact-name {
    color: var(--blue); font-weight: 700; font-size: 17px; letter-spacing: .3px;
    margin-bottom: 36px;
  }
  .contact-line {
    display: flex; align-items: center; gap: 7px;
    font-size: 12.5px; margin-bottom: 5px; white-space: nowrap;
  }
  .contact-line svg { width: 12px; height: 12px; flex: none; fill: var(--blue); }
  .services {
    position: absolute; left: 0; right: 0; bottom: 34px;
    text-align: center; font-size: 14px; line-height: 1.45;
  }
  .bullet {
    display: inline-block; width: 7px; height: 7px; border-radius: 50%;
    background: var(--red); margin: 0 6px; vertical-align: middle;
  }
  /* Back */
  .card-back .brand {
    position: absolute; left: 0; right: 0; top: 96px;
    display: flex; align-items: center; justify-content: center; gap: 9px;
  }
  .card-back .brand-dot { background: var(--silver); }
  .card-back .brand-name { color: var(--silver); }
  .thanks {
    position: absolute; left: 0; right: 0; top: 220px;
    text-align: center; font-size: 13px; letter-spacing: .3px; text-transform: uppercase;
  }
</style>
</head>
<body>
<main class="stage">
  <section class="card card-front" aria-label="Card front">
    <div class="brand">
      <span class="brand-dot"></span>
      <span class="brand-name">PINEGROVE</span>
    </div>
    <div class="divider"></div>
    <div class="contact">
      <p class="contact-name">TEODOR K (TED)</p>
      <p class="contact-line">
        <svg viewBox="0 0 24 24" aria-hidden="true"><path d="M6.6 10.8a15.2 15.2 0 0 0 6.6 6.6l2.2-2.2a1 1 0 0 1 1-.25 11.4 11.4 0 0 0 3.6.57 1 1 0 0 1 1 1V20a1 1 0 0 1-1 1A17 17 0 0 1 3 4a1 1 0 0 1 1-1h3.5a1 1 0 0 1 1 1c0 1.25.2 2.45.57 3.57a1 1 0 0 1-.25 1z"/></svg>
        555.284.9136
      </p>
      <p class="contact-line">
        <svg viewBox="0 0 24 24" aria-hidden="true"><path d="M2 5h20v14H2z"/><path d="M2 6l10 7 10-7" fill="none" stroke="#111" stroke-width="1.6"/></svg>
        Pinegrovehvac47@mailbox-example.com
      </p>
    </div>
    <div class="services">
      <p>Repairs, Installations, and maintenance<span class="bullet"></span>Residential/commercial</p>
      <p>Quality work at reasonable prices<span class="bullet"></span>Licensed &amp; Insured</p>
    </div>
  </section>

  <section class="card card-back" aria-label="Card back">
    <div class="brand">
      <span class="brand-dot"></span>
      <span class="brand-name">PINEGROVE</span>
    </div>
    <p class="thanks">Thank you for your business and refferal</p>
  </section>
</main>
</body>
</html>
```